Business Card, Stationery
Tax & Accounting Services
Professional
Lirena Vostrup EA
Tax Professional / Enrolled Agent
417 W Callory Avenue
Suite D
Halvern NY 10692
lvfiscalhub@quorvane.com
lvfiscalhub.com
Services:
Individual Tax Preparation
Business Tax Preparation
Tax Planning
DTB & State Tax Problems
Accounting
Payroll
Sales Tax
New Business Formation
Quickbooks Setup

```html
<!DOCTYPE html>
<html lang="en">
<head>
<meta charset="utf-8">
<title>LV Fiscal Hub Inc – Business Card</title>
<link href="https://fonts.googleapis.com/css2?family=Cormorant+SC:wght@500;600;700&display=swap" rel="stylesheet">
<style>
  :root {
    --page-bg: #e8e5df;
    --card-white: #ffffff;
    --brand-blue: #1c4f93;
    --brand-blue-dark: #0b2c63;
    --brand-blue-light: #4a86c8;
    --brand-red: #c81f2a;
    --ink-dark: #1d1d1f;
    --ink-light: #ffffff;
    --divider-grey: #6b6b70;
  }
  * { margin: 0; padding: 0; box-sizing: border-box; }
  html, body {
    width: 1200px; height: 778px; overflow: hidden;
    background: var(--page-bg);
  }
  .card {
    position: absolute; left: 80px; top: 62px;
    width: 1040px; height: 654px;
    border-radius: 34px; overflow: hidden;
    background: var(--card-white);
    box-shadow: 0 10px 30px rgba(0,0,0,0.18);
    font-family: "Cormorant SC", "Times New Roman", serif;
  }
  .card-wave { position: absolute; inset: 0; width: 100%; height: 100%; }
  .brand {
    position: absolute; left: 177px; top: 76px; height: 110px;
    display: flex; align-items: center;
  }
  .brand-mark {
    width: 92px; height: 92px; background: var(--brand-blue);
  }
  .brand-divider {
    width: 2px; height: 118px; background: var(--divider-grey);
    margin: 0 26px 0 46px;
  }
  .brand-name {
    font-size: 64px; font-weight: 600; color: var(--ink-dark);
    letter-spacing: 0.5px; white-space: nowrap;
  }
  .holder {
    position: absolute; left: 149px; top: 424px; width: 364px;
    color: var(--ink-light);
  }
  .holder-name { font-size: 34px; font-weight: 600; letter-spacing: 1px; line-height: 1.1; }
  .holder-title { font-size: 21px; font-weight: 600; letter-spacing: 0.5px; margin-top: 4px; }
  .holder-address {
    font-size: 25px; font-weight: 600; line-height: 34px; margin-top: 40px;
    letter-spacing: 0.3px; text-align: right; white-space: nowrap;
  }
  .contact-divider {
    position: absolute; left: 534px; top: 430px;
    width: 1.5px; height: 180px; background: rgba(255,255,255,0.75);
  }
  .contacts {
    position: absolute; left: 560px; top: 426px;
    list-style: none; color: var(--ink-light);
  }
  .contacts li {
    display: flex; align-items: center;
    height: 37px; font-size: 26px; font-weight: 600; letter-spacing: 0.5px;
  }
  .contacts svg { width: 18px; height: 18px; margin-right: 14px; fill: var(--ink-light); flex: none; }
</style>
</head>
<body>
  <article class="card">
    <svg class="card-wave" viewBox="0 0 1040 654" preserveAspectRatio="none" aria-hidden="true">
      <defs>
        <radialGradient id="blueGlow" cx="0.3" cy="0.55" r="0.75">
          <stop offset="0" stop-color="var(--brand-blue-light)"/>
          <stop offset="0.5" stop-color="var(--brand-blue)"/>
          <stop offset="1" stop-color="var(--brand-blue-dark)"/>
        </radialGradient>
      </defs>
      <path class="wave-red" d="M0 282 C 260 340, 560 300, 1040 206 L1040 232 C 600 320, 280 360, 0 312 Z" fill="var(--brand-red)"/>
      <path class="wave-blue" d="M0 300 C 280 356, 600 318, 1040 220 L1040 654 L0 654 Z" fill="url(#blueGlow)"/>
    </svg>

    <header class="brand">
      <div class="brand-mark"></div>
      <div class="brand-divider"></div>
      <h1 class="brand-name">LV Fiscal Hub Inc</h1>
    </header>

    <section class="holder">
      <p class="holder-name">Lirena Vostrup EA</p>
      <p class="holder-title">Tax Professional / Enrolled Agent</p>
      <p class="holder-address">417 W Callory Avenue, Suite D<br>Halvern NY 10692</p>
    </section>

    <div class="contact-divider"></div>

    <ul class="contacts">
      <li><svg viewBox="0 0 24 24"><path d="M6.6 10.8a15 15 0 0 0 6.6 6.6l2.2-2.2c.3-.3.7-.4 1-.2 1.1.4 2.3.6 3.6.6.6 0 1 .4 1 1V20c0 .6-.4 1-1 1A17 17 0 0 1 3 4c0-.6.4-1 1-1h3.5c.6 0 1 .4 1 1 0 1.3.2 2.5.6 3.6.1.3 0 .7-.2 1z"/></svg>347-555-0148</li>
      <li><svg viewBox="0 0 24 24"><path d="M7 1h10a2 2 0 0 1 2 2v18a2 2 0 0 1-2 2H7a2 2 0 0 1-2-2V3a2 2 0 0 1 2-2zm0 3v14h10V4z"/></svg>718-555-0193</li>
      <li><svg viewBox="0 0 24 24"><path d="M6 2h9l3 3v4H6zM3 10h18a1 1 0 0 1 1 1v9a1 1 0 0 1-1 1H3a1 1 0 0 1-1-1v-9a1 1 0 0 1 1-1zm3 3v2h4v-2zm0 4v2h4v-2z"/></svg>347-555-0176</li>
      <li><svg viewBox="0 0 24 24"><path d="M2 5h20v14H2zm2 2v.5l8 5 8-5V7zm0 2.9V17h16V9.9l-8 5z"/></svg>lvfiscalhub@quorvane.com</li>
      <li><svg viewBox="0 0 24 24"><path d="M12 2a10 10 0 1 0 0 20 10 10 0 0 0 0-20zm-1 17.9A8 8 0 0 1 4.1 11H8a14 14 0 0 0 3 8.9zM8 9H4.1A8 8 0 0 1 11 4.1 14 14 0 0 0 8 9zm3 0h2a12 12 0 0 0-1-4 12 12 0 0 0-1 4zm2 2h-2a12 12 0 0 0 1 7 12 12 0 0 0 1-7zm3-2a14 14 0 0 0-3-4.9A8 8 0 0 1 19.9 9zm0 2h3.9a8 8 0 0 1-6.9 6.9A14 14 0 0 0 16 11z"/></svg>www.lvfiscalhub.com</li>
    </ul>
  </article>
</body>
</html>
```